Packaging designed for both the bar and the box for retail and online sales

The name of the product is Plume Crumb. We manufacture a consumer package good product that's a healthy edible cookie dough bar. The product look, feels and tastes like cookie dough. It's sold in the refrigerator section of retail stores next to cookie dough and tundra loaf. The product is Gluten Free, Diary Free and include B-12, Biotin and Collagen. The ingredients are natural. When design this think about who eat cookie dough and how to engage the buyer in purchasing the product.

We needs design packaging designed for both the bar and the box. I have attached the die lines for both products.

Target Market(s)

Our customer is 16-45. Primarily female but really anyone. Middle to upper income. Interest include healthy life style and yoga. Like to eat something sweet but not feel guilty.

Colors

Designer to choose colors to be used in the design.

Requirements
Must have
• Must be clean, warm, inviting. Brand designs I really like are Tundra Loaf.
Should not have
• Should not have a photo of food

```html
<!DOCTYPE html>
<html lang="en">
<head>
<meta charset="utf-8">
<title>Plume Crumb – Front Panel</title>
<link href="https://fonts.googleapis.com/css2?family=Oswald:wght@500;700&family=Open+Sans:wght@400;600&display=swap" rel="stylesheet">
<style>
  :root {
    --stage: #d9d9d9;
    --red: #b3252c;
    --red-mid: #c33b30;
    --orange: #c9502f;
    --orange-deep: #b8452a;
    --logo-box: #871c22;
    --frame: #e8892c;
    --gold: #d7a21f;
    --gold-dark: #7a4b12;
    --ribbon: #f3c613;
    --band: #e0321f;
    --white: #ffffff;
    --cookie: #a8432a;
  }
  * { box-sizing: border-box; margin: 0; padding: 0; }
  html, body { width: 1200px; height: 818px; overflow: hidden; background: var(--stage); }
  .canvas { position: relative; width: 1200px; height: 818px; }
  .panel {
    position: absolute; left: 377px; top: 39px; width: 446px; height: 740px;
    overflow: hidden; background: var(--orange);
    font-family: "Open Sans", sans-serif; color: var(--white);
  }
  .panel-bg { position: absolute; inset: 0; }
  .ribbon {
    position: absolute; left: -44px; top: 22px; width: 150px; height: 26px;
    background: var(--ribbon); transform: rotate(-45deg);
    font-family: "Oswald", sans-serif; font-weight: 700; font-size: 17px;
    color: var(--white); text-align: center; line-height: 26px; letter-spacing: 1px;
  }
  .logo-box {
    position: absolute; left: 73px; top: 123px; width: 301px; height: 229px;
    background: var(--logo-box);
  }
  .logo-frame { position: absolute; left: 14px; top: 90px; width: 273px; height: 125px;
    border: 2px solid var(--frame); border-top: none; }
  .brand-name {
    position: absolute; left: 0; right: 0; top: 56px; text-align: center;
    font-family: "Oswald", sans-serif; font-weight: 700; font-size: 62px;
    line-height: 0.98; color: var(--white); text-transform: uppercase;
  }
  .benefits { position: absolute; left: 118px; top: 375px; display: flex; gap: 30px; }
  .benefit { width: 55px; text-align: center; font-size: 8px; letter-spacing: 0.4px; }
  .benefit-icon { display: block; margin: 0 auto 6px; }
  .cookie-art {
    position: absolute; left: 31px; top: 473px; width: 356px; height: 356px;
    border-radius: 50%; background: var(--cookie); opacity: 0.55;
    border: 6px solid rgba(150,55,35,0.6);
  }
  .free-list { position: absolute; left: 73px; top: 517px; }
  .free-item { display: flex; align-items: center; gap: 6px; margin-bottom: 14px;
    font-family: "Oswald", sans-serif; font-weight: 500; font-size: 15px; }
  .web-band {
    position: absolute; left: 0; top: 652px; width: 205px; height: 27px;
    background: var(--band); clip-path: polygon(0 0, 100% 0, 88% 100%, 0 100%);
    font-size: 13.5px; line-height: 27px; padding-left: 42px;
  }
  .nutrients { position: absolute; left: 229px; top: 586px; width: 176px; }
  .nutrients-title { font-family: "Oswald", sans-serif; font-weight: 500; font-size: 15px;
    padding-bottom: 4px; border-bottom: 2px solid var(--white); margin-bottom: 8px; }
  .nutrients-copy { font-size: 10px; line-height: 1.3; }
</style>
</head>
<body>
<main class="canvas">
  <section class="panel" aria-label="Plume Crumb box front">
    <svg class="panel-bg" width="446" height="740" viewBox="0 0 446 740">
      <rect width="446" height="740" fill="var(--orange)"/>
      <polygon points="0,0 446,0 446,300 0,230" fill="var(--red)"/>
      <polygon points="0,230 446,300 446,380 0,300" fill="var(--red-mid)" opacity="0.6"/>
      <polygon points="0,520 446,560 446,740 0,740" fill="var(--orange-deep)" opacity="0.5"/>
    </svg>
    <div class="ribbon">NEW</div>

    <div class="logo-box">
      <div class="logo-frame"></div>
      <div class="brand-name">Plume<br>Crumb</div>
    </div>

    <div class="benefits">
      <div class="benefit">
        <svg class="benefit-icon" width="30" height="30" viewBox="0 0 30 30"><circle cx="15" cy="15" r="14" fill="var(--gold)" stroke="var(--gold-dark)" stroke-width="1.5"/><path d="M8 20 L13 13 L16 17 L18 15 L22 20 Z" fill="none" stroke="var(--white)" stroke-width="1.5"/><circle cx="19" cy="10" r="1.8" fill="var(--white)"/></svg>
        LOREM IPSUM
      </div>
      <div class="benefit">
        <svg class="benefit-icon" width="30" height="30" viewBox="0 0 30 30"><circle cx="15" cy="15" r="14" fill="var(--gold)" stroke="var(--gold-dark)" stroke-width="1.5"/><path d="M8 20 L13 13 L16 17 L18 15 L22 20 Z" fill="none" stroke="var(--white)" stroke-width="1.5"/><circle cx="19" cy="10" r="1.8" fill="var(--white)"/></svg>
        LOREM IPSUM
      </div>
      <div class="benefit">
        <svg class="benefit-icon" width="30" height="30" viewBox="0 0 30 30"><circle cx="15" cy="15" r="14" fill="var(--gold)" stroke="var(--gold-dark)" stroke-width="1.5"/><path d="M8 20 L13 13 L16 17 L18 15 L22 20 Z" fill="none" stroke="var(--white)" stroke-width="1.5"/><circle cx="19" cy="10" r="1.8" fill="var(--white)"/></svg>
        LOREM IPSUM
      </div>
    </div>

    <div class="cookie-art" role="img" aria-label="Faint illustration of a bitten chocolate chip cookie"></div>

    <div class="free-list">
      <div class="free-item">
        <svg width="26" height="26" viewBox="0 0 26 26"><circle cx="13" cy="13" r="11.5" fill="none" stroke="var(--white)" stroke-width="1.6"/><line x1="5" y1="21" x2="21" y2="5" stroke="var(--white)" stroke-width="1.6"/></svg>
        GLUTEN FREE
      </div>
      <div class="free-item">
        <svg width="26" height="26" viewBox="0 0 26 26"><circle cx="13" cy="13" r="11.5" fill="none" stroke="var(--white)" stroke-width="1.6"/><line x1="5" y1="21" x2="21" y2="5" stroke="var(--white)" stroke-width="1.6"/></svg>
        DAIRY FREE
      </div>
    </div>

    <div class="web-band">www.plumecrumb.co</div>

    <div class="nutrients">
      <h2 class="nutrients-title">B-12, BIOTIN &amp; COLLAGEN</h2>
      <p class="nutrients-copy">Lorem ipsum dolor sit amet, consectetur adipiscing elit, sed do eiusmod tempor incididunt ut labore et dolore magna aliqua.</p>
    </div>
  </section>
</main>
</body>
</html>
```